Marrowfield Contracting Business Cards

Front of card:

Full Logo
Name
Address
Office Phone
Cell Phone
Email
Website

Back:
Logo Mark in background
List and markets and services performed

```html
<!DOCTYPE html>
<html lang="en">
<head>
<meta charset="utf-8">
<title>Marrowfield Contracting Business Cards</title>
<link href="https://fonts.googleapis.com/css2?family=Poppins:wght@300;400;600;700&display=swap" rel="stylesheet">
<style>
  :root {
    --red: #d92326;
    --red-dark: #b91e24;
    --ink: #222222;
    --grey-line: #cfcfcf;
    --backdrop: #dedede;
    --white: #ffffff;
  }
  * { margin: 0; padding: 0; box-sizing: border-box; }
  html, body { width: 1029px; height: 1200px; overflow: hidden; background: var(--backdrop); }
  body { font-family: "Poppins", sans-serif; }
  .stage { position: absolute; left: 0; top: 0; width: 1200px; height: 1400px; transform: scale(0.8575); transform-origin: 0 0; }
  .card { position: absolute; width: 833px; height: 481px; overflow: hidden; box-shadow: 0 6px 14px rgba(0,0,0,0.22); }

  /* Back: brand side */
  .card-brand { left: 182px; top: 162px; background: var(--red); color: var(--white); }
  .brand-mark { position: absolute; left: 226px; top: 184px; width: 114px; height: 114px; border-radius: 50%; border: 12px solid var(--white); }
  .brand-name { position: absolute; left: 360px; top: 196px; font-weight: 700; font-size: 33px; line-height: 38px; letter-spacing: 0.5px; text-transform: uppercase; }
  .services { position: absolute; left: 0; right: 0; top: 405px; text-align: center; font-weight: 300; font-size: 22px; }

  /* Front: contact side */
  .card-contact { left: 181px; top: 726px; background: var(--white); color: var(--ink); }
  .person { position: absolute; left: 58px; top: 58px; }
  .person-name { font-size: 30px; line-height: 36px; text-transform: uppercase; letter-spacing: -0.3px; }
  .person-name .first { font-weight: 700; }
  .person-name .last { font-weight: 300; }
  .person-role { font-size: 19px; font-weight: 300; line-height: 22px; }
  .person-rule { width: 72px; height: 4px; background: var(--red); margin-top: 6px; }

  .contact-mark { position: absolute; left: 508px; top: 60px; width: 80px; height: 80px; border-radius: 50%; background: var(--red); }
  .contact-brand { position: absolute; left: 600px; top: 68px; width: 174px; text-align: left; font-weight: 700; font-size: 22px; line-height: 28px; color: var(--red); text-transform: uppercase; letter-spacing: 0.2px; }

  .details { position: absolute; right: 108px; text-align: right; font-size: 17px; line-height: 21px; font-weight: 400; }
  .details.phone { top: 203px; }
  .details.email { top: 261px; }
  .details.web { top: 327px; }
  .details.address { top: 373px; color: var(--white); }
  .icon { position: absolute; left: 736px; width: 36px; height: 36px; }

  .decor { position: absolute; left: 0; top: 0; }
</style>
</head>
<body>
<div class="stage">

  <section class="card card-brand">
    <div class="brand-mark"></div>
    <div class="brand-name">Marrowfield<br>Contracting</div>
    <p class="services">List and markets and services performed</p>
  </section>

  <section class="card card-contact">
    <svg class="decor" width="833" height="481" viewBox="0 0 833 481">
      <polygon points="0,261 230,481 0,481" fill="var(--grey-line)"/>
      <polygon points="0,277 217,481 0,481" fill="var(--red-dark)"/>
      <polygon points="0,367 120,481 0,481" fill="var(--red)"/>
      <polygon points="98,367 146,367 179,399 833,399 833,481 217,481" fill="var(--ink)"/>
      <polygon points="341,361 833,361 833,425 404,425" fill="var(--red)"/>
    </svg>

    <div class="person">
      <h1 class="person-name"><span class="first">Dorian</span> <span class="last">Pell</span></h1>
      <p class="person-role">Solution Manager</p>
      <div class="person-rule"></div>
    </div>

    <div class="contact-mark"></div>
    <div class="contact-brand">Marrowfield<br>Contracting</div>

    <p class="details phone">123 . 456&nbsp; 78907890<br>123 . 456&nbsp; 78907890</p>
    <svg class="icon" style="top:197px" viewBox="0 0 36 36">
      <circle cx="18" cy="18" r="18" fill="var(--red)"/>
      <path d="M13 11c1-1 2 0 3 2s0 2-1 3c1 2 3 4 5 5 1-1 1-2 3-1s3 2 2 3-2 2-4 2c-4-1-8-5-9-9 0-2 0-4 1-5z" fill="var(--white)"/>
    </svg>

    <p class="details email">hello@marrowfieldco.com<br>office@marrowfieldco.com</p>
    <svg class="icon" style="top:261px" viewBox="0 0 36 36">
      <circle cx="18" cy="18" r="18" fill="var(--red)"/>
      <rect x="10" y="12" width="16" height="12" fill="none" stroke="var(--white)" stroke-width="1.8"/>
      <polyline points="10,12 18,19 26,12" fill="none" stroke="var(--white)" stroke-width="1.8"/>
    </svg>

    <p class="details web">www.marrowfieldco.com</p>
    <svg class="icon" style="top:320px" viewBox="0 0 36 36">
      <circle cx="18" cy="18" r="18" fill="var(--red)"/>
      <g fill="none" stroke="var(--white)" stroke-width="1.5">
        <circle cx="18" cy="18" r="8"/>
        <ellipse cx="18" cy="18" rx="3.5" ry="8"/>
        <line x1="10" y1="18" x2="26" y2="18"/>
        <line x1="11" y1="14" x2="25" y2="14"/>
        <line x1="11" y1="22" x2="25" y2="22"/>
      </g>
    </svg>

    <p class="details address">Address here,<br>Suite#1 Harlow Avenue, NY -012</p>
    <svg class="icon" style="top:376px" viewBox="0 0 36 36">
      <path d="M18 3c-6 0-10 4.5-10 10 0 7 10 19 10 19s10-12 10-19c0-5.5-4-10-10-10z" fill="var(--white)"/>
      <circle cx="18" cy="13" r="3.8" fill="var(--red)"/>
    </svg>
  </section>

</div>
</body>
</html>
```